Infografik im Bereich Artikelbeschreibung für Onlineshop
Zielgruppe
Vertrieb von Saunaaustattung
Aufgabenstellung
Wird als Ergänzung für die Artikelbeschreibung im Webshop benötigt.
Ein Beispiel wo die Infografik platziert werden soll:
https://www.wellforumtech.example/Bilder/beispiel.jpg
Bildgröße ca. 1200 x 800 px
Als Hintergrund eventuell möglich teilweise oder ganz die Grafik mit den blauen Wassertropfen verwendbar?

```html
<!DOCTYPE html>
<html lang="de">
<head>
<meta charset="utf-8">
<title>Dampfgenerator – Ausstattungsmerkmale</title>
<link rel="stylesheet" href="https://fonts.googleapis.com/css2?family=Roboto+Condensed:wght@700&display=swap">
<style>
  :root{
    --orange-a:#f26b21; --orange-b:#fbb216;
    --purple-a:#8a2a8c; --purple-b:#e5177e;
    --blue-a:#1b6fb8; --blue-b:#28b0e6;
    --green-a:#2f9a3a; --green-b:#8dc63f;
    --red-a:#c2141c; --red-b:#ee2a24;
    --magenta-a:#e2197c; --magenta-b:#8b2a8e;
    --white:#ffffff;
    --line:rgba(255,255,255,.92);
  }
  *{margin:0;padding:0;box-sizing:border-box}
  html,body{width:1200px;height:800px;overflow:hidden}
  body{font-family:"Roboto Condensed","Arial Narrow",sans-serif;font-weight:700;color:var(--white);text-transform:uppercase}
  .canvas{position:relative;width:1200px;height:800px;overflow:hidden}
  .backdrop{position:absolute;inset:0;
    background:radial-gradient(ellipse at 50% 40%,#9fd3ee 0%,#5fa8d6 45%,#2f6fa8 100%)}
  .connectors{position:absolute;inset:0}
  .hub{position:absolute;left:400px;top:215px;width:400px;height:400px;border-radius:50%;
    background:conic-gradient(#f7a81b,#ef4123,#e5177e,#8a2a8c,#1b6fb8,#28b0e6,#3aaa35,#8dc63f,#f7a81b);
    padding:12px}
  .hub-inner{width:100%;height:100%;border-radius:50%;background:var(--white);display:flex;align-items:center;justify-content:center}
  .product-photo{width:290px;height:250px;border-radius:6px;
    background:linear-gradient(135deg,#e6e8ea 0%,#b9bec3 55%,#8d9398 100%)}

  .pill{position:absolute;height:90px;display:flex;align-items:center;font-size:20px;line-height:1.25;letter-spacing:0}
  .pill--left{left:0;width:325px;border-radius:0 45px 45px 0;padding-left:30px;padding-right:96px}
  .pill--right{right:0;width:345px;border-radius:45px 0 0 45px;padding-left:115px}
  .pill .badge{position:absolute;top:7px;width:76px;height:76px;border-radius:50%;background:var(--white);
    display:flex;align-items:center;justify-content:center;box-shadow:0 1px 3px rgba(0,0,0,.25)}
  .pill--left .badge{right:7px}
  .pill--right .badge{left:7px}
  .badge svg{width:48px;height:48px}
  .badge .photo{width:66px;height:66px;border-radius:50%;background:radial-gradient(circle,#f2f2f2,#9aa0a6)}

  .tab{position:absolute;width:86px;display:flex;flex-direction:column;align-items:center;text-align:center;font-size:10px;line-height:1.25}
  .tab--top{top:0;height:136px;border-radius:0 0 43px 43px;padding-top:18px}
  .tab--top .badge{position:absolute;bottom:6px}
  .tab--bottom{bottom:0;height:150px;border-radius:43px 43px 0 0;justify-content:flex-end;padding-bottom:20px;font-size:9px}
  .tab--bottom .badge{position:absolute;top:6px}
  .tab .badge{width:72px;height:72px;border-radius:50%;background:var(--white);display:flex;align-items:center;justify-content:center}
  .tab .badge svg{width:44px;height:44px}

  .c-orange{background:linear-gradient(90deg,var(--orange-a),var(--orange-b))}
  .c-purple{background:linear-gradient(90deg,var(--purple-a),var(--purple-b))}
  .c-blue{background:linear-gradient(90deg,var(--blue-a),var(--blue-b))}
  .c-green{background:linear-gradient(90deg,var(--green-a),var(--green-b))}
  .c-red{background:linear-gradient(90deg,var(--red-b),var(--red-a))}
  .c-magenta{background:linear-gradient(90deg,var(--magenta-a),var(--magenta-b))}
  .pill--right.c-orange{background:linear-gradient(90deg,var(--orange-b),var(--orange-a))}
  .pill--right.c-green{background:linear-gradient(90deg,var(--green-b),var(--green-a))}
  .pill--right.c-blue{background:linear-gradient(90deg,var(--blue-b),var(--blue-a))}
  .tab.c-orange{background:linear-gradient(180deg,var(--orange-a),var(--orange-b))}
  .tab.c-green{background:linear-gradient(180deg,var(--green-a),var(--green-b))}
  .tab.c-blue{background:linear-gradient(180deg,var(--blue-a),var(--blue-b))}
  .tab.c-red{background:linear-gradient(180deg,var(--red-a),var(--red-b))}
</style>
</head>
<body>
<main class="canvas">
  <div class="backdrop" role="img" aria-label="Hintergrund: beschlagene Glasscheibe mit blauen Wassertropfen"></div>

  <svg class="connectors" viewBox="0 0 1200 800" stroke="var(--line)" stroke-width="4" fill="none" aria-hidden="true">
    <line x1="320" y1="175" x2="450" y2="245"/>
    <line x1="320" y1="295" x2="410" y2="320"/>
    <line x1="320" y1="400" x2="400" y2="400"/>
    <line x1="320" y1="525" x2="410" y2="500"/>
    <line x1="320" y1="635" x2="450" y2="570"/>
    <line x1="860" y1="165" x2="745" y2="245"/>
    <line x1="860" y1="285" x2="790" y2="315"/>
    <line x1="860" y1="400" x2="800" y2="400"/>
    <line x1="860" y1="515" x2="790" y2="500"/>
    <line x1="860" y1="630" x2="745" y2="575"/>
  </svg>

  <div class="hub"><div class="hub-inner">
    <div class="product-photo" role="img" aria-label="Produktfoto: Dampfgenerator im Edelstahlgehäuse mit Anschlüssen"></div>
  </div></div>

  <!-- Linke Merkmale -->
  <div class="pill pill--left c-orange" style="top:115px"><span>Inkludierte<br>Armoaauslassdüse</span>
    <span class="badge"><svg viewBox="0 0 48 48" fill="none" stroke="#28a9e0" stroke-width="2.5" stroke-linecap="round"><circle cx="24" cy="20" r="9" fill="#28a9e0"/><path d="M24 6v3M14 34l-4 6M20 36l-1 6M28 36l1 6M34 34l4 6"/></svg></span></div>
  <div class="pill pill--left c-purple" style="top:232px"><span>Kurze Aufheizzeit</span>
    <span class="badge"><svg viewBox="0 0 48 48" fill="none" stroke="#8a2a8c" stroke-width="2.5"><circle cx="24" cy="24" r="19" stroke-dasharray="4 3"/><text x="24" y="23" font-size="10" text-anchor="middle" fill="#8a2a8c" stroke="none" font-family="Roboto Condensed,sans-serif">4 - 8</text><text x="24" y="34" font-size="9" text-anchor="middle" fill="#8a2a8c" stroke="none" font-family="Roboto Condensed,sans-serif">min</text></svg></span></div>
  <div class="pill pill--left c-blue" style="top:352px"><span>Ansteuerung von bis<br>zu zwei Duftstoffen</span>
    <span class="badge"><svg viewBox="0 0 48 48" fill="#28a9e0"><circle cx="17" cy="28" r="7"/><circle cx="31" cy="28" r="7"/><circle cx="24" cy="17" r="5"/><text x="3" y="36" font-size="11" font-family="Roboto Condensed,sans-serif">A</text><text x="38" y="36" font-size="11" font-family="Roboto Condensed,sans-serif">B</text></svg></span></div>
  <div class="pill pill--left c-green" style="top:472px"><span>Optional<br>Steuerung per App</span>
    <span class="badge"><svg viewBox="0 0 48 48" fill="none" stroke="#28a9e0" stroke-width="2.5" stroke-linejoin="round"><rect x="12" y="5" width="22" height="36" rx="3"/><path d="M24 22v14l-4-3-2 3 7 7h10l2-10-8-3v-8z" fill="#fff"/></svg></span></div>
  <div class="pill pill--left c-orange" style="top:595px"><span>Elektronische<br>Entkalkung</span>
    <span class="badge"><svg viewBox="0 0 48 48" fill="none" stroke="#28a9e0" stroke-width="2.5" stroke-linejoin="round"><path d="M16 8v16H9l15 17 15-17h-7V8"/><circle cx="21" cy="18" r="2"/><circle cx="27" cy="24" r="2"/><circle cx="22" cy="28" r="1.5"/></svg></span></div>

  <!-- Rechte Merkmale -->
  <div class="pill pill--right c-orange" style="top:110px"><span>Manuelles<br>Entkalken</span>
    <span class="badge"><span class="photo" role="img" aria-label="Foto: Entkalkungsöffnung"></span></span></div>
  <div class="pill pill--right c-red" style="top:228px"><span>Gehäuse<br>Edelstahl<br>S304</span></div>
  <div class="pill pill--right c-green" style="top:350px"><span>Hochleistungs-<br>heizstäbe</span>
    <span class="badge"><span class="photo" role="img" aria-label="Foto: Heizstab"></span></span></div>
  <div class="pill pill--right c-blue" style="top:470px"><span>Elektronisches<br>Abflussventil</span>
    <span class="badge"><span class="photo" role="img" aria-label="Foto: Abflussventil"></span></span></div>
  <div class="pill pill--right c-magenta" style="top:592px;height:96px"><span>Steuerdisplay<br>fliesenbündig<br>einbaubar</span></div>

  <!-- Obere Reiter -->
  <div class="tab tab--top c-blue" style="left:328px">Thermoschutz
    <span class="badge"><svg viewBox="0 0 48 48" fill="none" stroke="#28a9e0" stroke-width="2.5"><path d="M24 5l15 5v12c0 10-7 17-15 21-8-4-15-11-15-21V10z"/><path d="M24 15v13"/><circle cx="24" cy="31" r="3" fill="#28a9e0"/></svg></span></div>
  <div class="tab tab--top c-orange" style="left:466px">Automatische<br>Selbstreinigung
    <span class="badge"><svg viewBox="0 0 48 48" fill="none" stroke="#28a9e0" stroke-width="2.5" stroke-linecap="round"><path d="M38 8L26 22"/><path d="M26 22c-6-2-12 2-14 10l6 8c8-2 12-8 10-14z" fill="#28a9e0"/></svg></span></div>
  <div class="tab tab--top c-green" style="left:612px">Kompakte<br>Größe
    <span class="badge"><svg viewBox="0 0 48 48" fill="none" stroke="#28a9e0" stroke-width="2"><rect x="8" y="8" width="32" height="32" stroke-dasharray="3 2"/><text x="24" y="29" font-size="11" text-anchor="middle" fill="#28a9e0" stroke="none" font-family="Roboto Condensed,sans-serif">cm²</text></svg></span></div>
  <div class="tab tab--top c-blue" style="left:760px">Gerät kocht auf<br>ca. 100 C° hoch
    <span class="badge"><svg viewBox="0 0 48 48" fill="none" stroke="#28a9e0" stroke-width="2.5"><circle cx="24" cy="24" r="18"/><circle cx="24" cy="24" r="7"/><path d="M11 11l26 26"/></svg></span></div>

  <!-- Untere Reiter -->
  <div class="tab tab--bottom c-orange" style="left:328px">Farblichtsteuerung
    <span class="badge"><svg viewBox="0 0 48 48" fill="none" stroke="#f26b21" stroke-width="2.5" stroke-linejoin="round"><path d="M17 30c-4-3-6-7-6-11a13 13 0 0126 0c0 4-2 8-6 11v4H17z"/><path d="M18 38h12M20 42h8"/></svg></span></div>
  <div class="tab tab--bottom c-green" style="left:466px">Ansteuerung<br>Salzsolevernebler
    <span class="badge"><svg viewBox="0 0 48 48" fill="none" stroke="#3aaa35" stroke-width="2.5"><path d="M20 8l14 8-8 14-14-8z" fill="#3aaa35"/><circle cx="16" cy="34" r="1.5" fill="#3aaa35"/><circle cx="12" cy="40" r="1.5" fill="#3aaa35"/><circle cx="19" cy="41" r="1.5" fill="#3aaa35"/></svg></span></div>
  <div class="tab tab--bottom c-red" style="left:612px">Verbrühschutz<br>Abfluss
    <span class="badge"><svg viewBox="0 0 48 48" fill="none" stroke="#c2141c" stroke-width="2.5"><path d="M20 30V8a4 4 0 018 0v22"/><circle cx="24" cy="35" r="7" fill="#c2141c"/><path d="M24 14v16" stroke-width="4"/></svg></span></div>
  <div class="tab tab--bottom c-blue" style="left:760px">Integrierte<br>Abluftsteuerung
    <span class="badge"><svg viewBox="0 0 48 48" fill="none" stroke="#1b6fb8" stroke-width="2.5"><circle cx="24" cy="24" r="19"/><circle cx="24" cy="24" r="3"/><path d="M24 21c-2-6 0-11 5-11 3 6-2 9-5 11zM27 25c6-1 10 2 9 7-7 1-8-4-9-7zM21 26c-4 5-9 6-11 2 3-6 8-4 11-2z"/></svg></span></div>
</main>
</body>
</html>
```